Business Card for a recruitment agency specializing in engineers and geeks.

I am looking to create Business Card Design for my company.
That
## Company name:
Vornplick Inc.
Vornplick is a term coined from the following concepts.
1. geek + engineer
2. geek utopia
## Company Description:
The concept of the company is to be a recruitment agency that creates a paradise for geeky engineers. We want to be a place where engineers can have more freedom and ideal career support.
# Target.
The noun itself is often given to companies that want to hire engineers, geeks, and IT-related personnel, so it would be nice to get the impression that this company seems to have good engineers and IT personnel. There are many occasions where I meet with the human resources department, president, or senior management and give it to them.
# Atmosphere
We are happy with simplicity, but with an impact that will help people remember the company. The logo is based on a dinosaur that does programming, so it should be somewhat playful, but since it will basically be used in a business setting, please don't make it too silly.
# About the logo
See the attached files. The company logo represents our engineers smiling upward because of our work, with the motif of a dinosaur doing programming.
## Color
We will leave the color scheme to you, but since the logo is in black and white, colors with such a taste would fit well.
## file format
ai, psd, png, svg
Industry/Entity Type
human resource and employment agency
Contact Information for Business Card
Company name, address, email, tel, URL,logo
Colors
Designer to choose colors to be used in the design.
Look and feel
Each slider illustrates characteristics of the customer's brand and the style your logo design should communicate.

```html
<!DOCTYPE html>
<html lang="en">
<head>
<meta charset="utf-8">
<title>Vornplick Inc. — Business Card</title>
<link rel="stylesheet" href="https://fonts.googleapis.com/css2?family=Ubuntu:wght@500;700&family=Roboto:wght@400&display=swap">
<style>
  :root {
    --backdrop: #2b2b2b;
    --card-light: #f3f3f3;
    --card-mid: #e2e2e2;
    --ink: #111111;
    --ink-soft: #222222;
  }
  html, body {
    margin: 0;
    padding: 0;
    width: 1200px;
    height: 1138px;
    overflow: hidden;
    background: var(--backdrop);
  }
  .canvas {
    position: relative;
    width: 1200px;
    height: 1138px;
  }
  .card {
    position: absolute;
    width: 620px;
    height: 372px;
    border-radius: 14px;
    background: linear-gradient(160deg, var(--card-light) 0%, #ebebeb 55%, var(--card-mid) 100%);
  }
  .card-front { left: 274px; top: 186px; }
  .card-back  { left: 276px; top: 608px; }

  .brand {
    position: absolute;
    left: 0; right: 0;
    top: 148px;
    display: flex;
    justify-content: center;
    align-items: center;
    gap: 18px;
  }
  .brand-mark {
    width: 34px;
    height: 34px;
    background: var(--ink);
  }
  .brand-name {
    font-family: "Ubuntu", sans-serif;
    font-weight: 500;
    font-size: 54px;
    line-height: 1;
    color: var(--ink);
  }
  .front-url {
    position: absolute;
    left: 0; right: 0;
    top: 334px;
    display: flex;
    justify-content: center;
    align-items: center;
    gap: 14px;
    font-family: "Roboto", sans-serif;
    font-size: 15px;
    color: var(--ink-soft);
  }
  .front-url .rule {
    width: 62px;
    height: 1.5px;
    background: var(--ink-soft);
  }

  .holder {
    position: absolute;
    left: 0; right: 0;
    top: 254px;
    text-align: center;
    font-family: "Ubuntu", sans-serif;
    font-weight: 700;
    font-size: 23px;
    color: var(--ink-soft);
  }
  .contact {
    position: absolute;
    left: 0; right: 0;
    top: 294px;
    text-align: center;
    font-family: "Roboto", sans-serif;
    font-size: 15px;
    line-height: 24px;
    color: var(--ink-soft);
  }
  .contact p { margin: 0; }
  .contact .sep { margin: 0 7px; }
</style>
</head>
<body>
<div class="canvas">
  <section class="card card-front">
    <div class="brand">
      <span class="brand-mark" aria-hidden="true"></span>
      <span class="brand-name">Vornplick</span>
    </div>
    <div class="front-url">
      <span class="rule"></span>
      <span>www.vornplick.com</span>
      <span class="rule"></span>
    </div>
  </section>

  <section class="card card-back">
    <div class="holder">Elin Tessaro</div>
    <div class="contact">
      <p>P.: 000-111-1111<span class="sep">|</span>E: elin@vornplick.com<span class="sep">|</span>W: www.vornplick.com</p>
      <p>234 Anywhere St., Any City, Any Town, US 123456</p>
    </div>
  </section>
</div>
</body>
</html>
```